KTV Catapult

I need a graphic package design for our new bodybuilding sports supplement. The artwork should be clean and useable for many formats. examples or great usage are www.brawnvelta.example, www.sinewcore.example and http://www.pellarynutrition.example/ as examples. I am adding our logo for your reference. The name Catapult is because it will help make "Big Guns" as a catch phrase, the product line will have other supplements such as creatine and protein powders and the artwork should be useable on all products. You can see our website for ideas at www.kestovalelabs.example
Updates

Hi everyone, There are some nice entries coming in. I do wonder if some of you are reading the brief as a few labels don't even highlight the product, KTV is the company, Catapult is the Product. Thanks Dex

Industry/Entity Type

Supplement

```html
<!DOCTYPE html>
<html lang="en">
<head>
<meta charset="utf-8">
<title>KTV Catapult Protein Powder Label</title>
<link rel="stylesheet" href="https://fonts.googleapis.com/css2?family=Exo+2:wght@700&family=Oswald:wght@500;600&display=swap">
<style>
  :root {
    --page: #ffffff;
    --label-black: #141414;
    --green-dark: #356b2c;
    --green-mid: #5fa04a;
    --green-light: #a8dc8a;
    --white: #ffffff;
    --grey-text: #d4d4d4;
    --side-text: #eef7e8;
  }
  html, body {
    margin: 0;
    width: 1200px;
    height: 848px;
    overflow: hidden;
    background: var(--page);
  }
  .canvas {
    position: relative;
    width: 1200px;
    height: 848px;
  }
  .label {
    position: absolute;
    left: 150px;
    top: 174px;
    width: 900px;
    height: 500px;
    overflow: hidden;
  }
  .label-art {
    position: absolute;
    inset: 0;
  }
  .brand {
    position: absolute;
    left: 220px;
    width: 460px;
    top: 36px;
    text-align: center;
    font-family: "Exo 2", sans-serif;
    font-weight: 700;
    color: var(--white);
  }
  .brand-name {
    font-size: 132px;
    line-height: 1;
    letter-spacing: 4px;
  }
  .brand-company {
    margin-top: 6px;
    font-size: 26px;
    letter-spacing: 3px;
  }
  .product-bar {
    position: absolute;
    left: 220px;
    width: 460px;
    top: 296px;
    height: 48px;
    display: flex;
    align-items: center;
    justify-content: center;
    font-family: "Oswald", sans-serif;
    font-weight: 600;
    font-size: 26px;
    letter-spacing: 3px;
    color: var(--white);
    white-space: nowrap;
  }
  .product-name {
    color: var(--green-light);
    margin-right: 12px;
  }
  .tagline {
    position: absolute;
    left: 220px;
    width: 460px;
    top: 366px;
    margin: 0;
    text-align: center;
    font-family: "Oswald", sans-serif;
    font-weight: 500;
    font-size: 21px;
    line-height: 1.35;
    letter-spacing: 2px;
    color: var(--grey-text);
    text-transform: uppercase;
  }
  .directions {
    position: absolute;
    left: 34px;
    top: 150px;
    width: 150px;
    font-family: "Oswald", sans-serif;
    font-weight: 500;
    font-size: 13px;
    line-height: 1.45;
    color: var(--side-text);
  }
  .directions h2 {
    margin: 0 0 6px;
    font-size: 15px;
    font-weight: 600;
    letter-spacing: 1px;
  }
  .directions p { margin: 0; }
</style>
</head>
<body>
<main class="canvas">
  <section class="label">
    <svg class="label-art" width="900" height="500" viewBox="0 0 900 500" aria-hidden="true">
      <defs>
        <linearGradient id="side-green" x1="0" y1="0" x2="1" y2="1">
          <stop offset="0" stop-color="var(--green-dark)"/>
          <stop offset="0.5" stop-color="var(--green-mid)"/>
          <stop offset="1" stop-color="var(--green-dark)"/>
        </linearGradient>
        <linearGradient id="swoosh-green" x1="0" y1="0" x2="1" y2="0">
          <stop offset="0" stop-color="var(--green-dark)"/>
          <stop offset="0.55" stop-color="var(--green-light)"/>
          <stop offset="1" stop-color="var(--green-mid)"/>
        </linearGradient>
      </defs>
      <rect class="side-panel" x="0" y="0" width="900" height="500" fill="url(#side-green)"/>
      <rect class="front-panel" x="220" y="0" width="460" height="500" fill="var(--label-black)"/>
      <path class="swoosh" d="M0 300 C 260 300 520 250 900 140 L 900 190 C 560 290 300 332 0 332 Z" fill="url(#swoosh-green)" opacity="0.9"/>
      <path class="swoosh-line" d="M0 286 C 260 284 520 236 900 124" fill="none" stroke="var(--green-light)" stroke-width="3"/>
      <rect class="product-band" x="220" y="296" width="460" height="48" fill="var(--label-black)"/>
      <rect x="220" y="292" width="460" height="3" fill="var(--green-light)"/>
      <rect x="220" y="345" width="460" height="3" fill="var(--green-light)"/>
      <rect x="0" y="300" width="220" height="40" fill="var(--green-mid)" opacity="0.6"/>
      <rect x="680" y="300" width="220" height="40" fill="var(--green-mid)" opacity="0.6"/>
      <g class="facts-table" stroke="var(--side-text)" stroke-width="1.5" opacity="0.8">
        <line x1="710" y1="230" x2="870" y2="230"/>
        <line x1="710" y1="260" x2="870" y2="260"/>
        <line x1="710" y1="290" x2="870" y2="290"/>
        <line x1="710" y1="360" x2="870" y2="360"/>
        <line x1="710" y1="390" x2="870" y2="390"/>
        <line x1="710" y1="420" x2="870" y2="420"/>
      </g>
    </svg>

    <div class="brand">
      <div class="brand-name">KTV</div>
      <div class="brand-company">KESTOVALE LABS</div>
    </div>

    <div class="product-bar"><span class="product-name">CATAPULT</span>PROTEIN POWDER</div>

    <p class="tagline">Launch your training further,<br>catapult your way to big guns.</p>

    <div class="directions">
      <h2>DIRECTIONS</h2>
      <p>Mix one scoop with 250 ml of water or milk. Shake well and drink after training. Store in a cool dry place. Keep out of reach of children.</p>
    </div>
  </section>
</main>
</body>
</html>
```